Business Card and Letterhead for Vantage Psychology

We need a business card design and letterhead to use for our Psychology firm that specializes in psychoeducational assessments and individual therapy. Our motto is Purpose-Driven Assessments, Meaning-Centered Therapy.Our contact information is as follows:
Vantage Psychology
The Marwick Block - 6127-48St.
Box 2716 Olds, AB
T2K 3M8
t 403.555.0148 (VANT)
f 403.555.0172
www.vantagepsychology-example.ca
The business card will be used for two different psychologists so I can supply names nearer to completion. We prefer clean, uncluttered looks.

Target Market(s)

Clients, Educators

Font styles to use
Sans Serif

Colors

Designer to choose colors to be used in the design.

Requirements
Must have
• All relevant contact info, logo, some "white" space.
Nice to have
• It would be nice to see letterhead options that have the logo on the top of the page but also options that have it on the side. I think top of the page is probably our preference.
Should not have
• Too much clutter!

```html
<!DOCTYPE html>
<html lang="en">
<head>
<meta charset="utf-8">
<title>Vantage Psychology – Letterhead and Business Card</title>
<link rel="stylesheet" href="https://fonts.googleapis.com/css2?family=Arimo:wght@400;700&display=swap">
<style>
  :root {
    --orange: #ff6a0c;
    --teal: #66efe4;
    --watermark: #fdede4;
    --ink: #111111;
    --paper: #ffffff;
    --backdrop: #e9e7e4;
  }
  * { box-sizing: border-box; margin: 0; padding: 0; }
  html, body { width: 848px; height: 1200px; overflow: hidden; }
  body {
    background: var(--backdrop);
    font-family: "Arimo", Arial, sans-serif;
    color: var(--ink);
    position: relative;
  }
  .icon-defs { position: absolute; width: 0; height: 0; }
  .icon { width: 14px; height: 14px; fill: none; stroke: var(--orange); stroke-width: 1.6; flex: none; }

  /* Letterhead */
  .letterhead {
    position: absolute; left: 174px; top: 40px;
    width: 500px; height: 707px;
    background: var(--paper);
    overflow: hidden;
    box-shadow: 0 2px 8px rgba(0,0,0,.12);
  }
  .letterhead__top-band { position: absolute; left: 0; top: 0; width: 100%; height: 8px; background: var(--orange); }
  .letterhead__brand {
    position: absolute; left: 30px; top: 30px;
    display: flex; flex-direction: column; align-items: center; gap: 8px;
  }
  .brand-dot { width: 40px; height: 40px; border-radius: 50%; background: var(--teal); flex: none; }
  .brand-name { font-weight: 700; font-size: 14px; letter-spacing: .06em; text-transform: uppercase; color: var(--orange); white-space: nowrap; }
  .letterhead__contact {
    position: absolute; right: 22px; top: 40px;
    border-left: 2px solid var(--orange);
    padding-left: 14px;
    display: flex; flex-direction: column; gap: 7px;
    font-size: 10.5px;
  }
  .contact-row { display: flex; align-items: center; gap: 8px; white-space: nowrap; }
  .letterhead__watermark {
    position: absolute; left: 160px; top: 300px;
    width: 190px; height: 190px; border-radius: 50%;
    background: var(--watermark);
  }
  .letterhead__address {
    position: absolute; left: 24px; bottom: 34px;
    font-style: normal;
    font-weight: 700; font-size: 9.5px; letter-spacing: .28em;
    line-height: 1.5; text-align: center;
  }
  .letterhead__accent {
    position: absolute; right: 0; bottom: 14px; width: 230px; height: 28px;
    background: var(--teal);
    clip-path: polygon(14% 0, 100% 0, 100% 100%, 0 100%);
  }
  .letterhead__bottom-band { position: absolute; left: 0; bottom: 0; width: 100%; height: 14px; background: var(--orange); }

  /* Business cards */
  .card {
    position: absolute; top: 800px; width: 360px; height: 206px;
    box-shadow: 0 2px 8px rgba(0,0,0,.12);
    overflow: hidden;
  }
  .card--front { left: 40px; background: var(--paper); }
  .card--back { left: 448px; background: var(--orange); }
  .card__identity {
    position: absolute; left: 22px; top: 22px;
    border-left: 2px solid var(--orange); padding-left: 10px;
    font-size: 9.5px; line-height: 1.6; letter-spacing: .06em;
  }
  .card__firm { font-size: 13px; color: var(--orange); letter-spacing: 0; }
  .card__brand { position: absolute; right: 18px; top: 30px; display: flex; flex-direction: column; align-items: center; gap: 6px; }
  .card__brand .brand-dot { width: 34px; height: 34px; }
  .card__brand .brand-name { font-size: 11px; }
  .card__contact { position: absolute; left: 24px; bottom: 20px; display: flex; flex-direction: column; gap: 5px; font-size: 9.5px; }
  .card__bottom-band { position: absolute; left: 0; bottom: 0; width: 100%; height: 4px; background: var(--orange); }

  .card--back .back-brand { position: absolute; inset: 0; display: flex; flex-direction: column; align-items: center; justify-content: center; gap: 18px; }
  .card--back .brand-dot { width: 70px; height: 70px; background: var(--paper); }
  .card--back .brand-name { color: var(--paper); font-size: 20px; }
</style>
</head>
<body>
<svg class="icon-defs" aria-hidden="true">
  <symbol id="icon-phone" viewBox="0 0 16 16"><path d="M2 6c0-2 3-3 6-3s6 1 6 3l-2 1-1-2H5L4 7z"/><rect x="4" y="8" width="8" height="6" rx="1"/></symbol>
  <symbol id="icon-fax" viewBox="0 0 16 16"><rect x="2" y="6" width="12" height="8"/><path d="M5 6V1h6v5M7 9h5M7 11h5"/></symbol>
  <symbol id="icon-web" viewBox="0 0 16 16"><circle cx="8" cy="8" r="6.5"/><ellipse cx="8" cy="8" rx="3" ry="6.5"/><path d="M1.5 8h13M3 4.5h10M3 11.5h10"/></symbol>
</svg>

<section class="letterhead" aria-label="Letterhead">
  <div class="letterhead__top-band"></div>
  <div class="letterhead__brand">
    <span class="brand-dot"></span>
    <span class="brand-name">Vantage Psychology</span>
  </div>
  <div class="letterhead__contact">
    <div class="contact-row"><svg class="icon"><use href="#icon-phone"/></svg>403.555.0148 (VANT)</div>
    <div class="contact-row"><svg class="icon"><use href="#icon-fax"/></svg>403.555.0172</div>
    <div class="contact-row"><svg class="icon"><use href="#icon-web"/></svg>www.vantagepsychology-example.ca</div>
  </div>
  <div class="letterhead__watermark"></div>
  <address class="letterhead__address">
    The Marwick Block - 6127-48St.<br>Box 2716 Olds, AB<br>T2K 3M8
  </address>
  <div class="letterhead__accent"></div>
  <div class="letterhead__bottom-band"></div>
</section>

<section class="card card--front" aria-label="Business card front">
  <div class="card__identity">
    <div class="card__firm">Vantage Psychology</div>
    The Marwick Block - 6127-48St.<br>Box 2716 Olds, AB<br>T2K 3M8
  </div>
  <div class="card__brand">
    <span class="brand-dot"></span>
    <span class="brand-name">Vantage Psychology</span>
  </div>
  <div class="card__contact">
    <div class="contact-row"><svg class="icon"><use href="#icon-phone"/></svg>403.555.0148 (VANT)</div>
    <div class="contact-row"><svg class="icon"><use href="#icon-fax"/></svg>403.555.0172</div>
    <div class="contact-row"><svg class="icon"><use href="#icon-web"/></svg>www.vantagepsychology-example.ca</div>
  </div>
  <div class="card__bottom-band"></div>
</section>

<section class="card card--back" aria-label="Business card back">
  <div class="back-brand">
    <span class="brand-dot"></span>
    <span class="brand-name">Vantage Psychology</span>
  </div>
</section>
</body>
</html>
```